Business Card Design

Buy and sell properties
Buy and rehab properties
Buy properties for cash
That is what I do but do need a logo
looking for some type of logo or design on it
Just started business
Back of card should say something like BUY HOUSES CASH
Overview: it is a new company. Basically I buy properties wholesale and fix them up and sell them or sell them to other fix and flippers
Background: company is new so not any background
Market: is basically anyone selling a house or buying a house. Someone that needs to sell house fast. Basically I am a cash home buyer!!!

Updates
Email on card should be:   harborlanerealtyinc@mailbox.test

Industry/Entity Type
House
Contact Information for Business Card
Harbor Lane Realty Inc
PO Box 718269
Cedar Marsh FL 32987

Dale Morrick
dmorrick@mailbox.test
555-271-6094

```html
<!DOCTYPE html>
<html lang="en">
<head>
<meta charset="utf-8">
<title>Harbor Lane Realty Inc – Business Card</title>
<link rel="stylesheet" href="https://fonts.googleapis.com/css2?family=Open+Sans:wght@400;600&display=swap">
<style>
  :root {
    --page: #ffffff;
    --card-dark: #2a2a2a;
    --card-mid: #3b3b3b;
    --sheen: rgba(255, 255, 255, 0.07);
    --sheen-strong: rgba(255, 255, 255, 0.11);
    --band-light: #ffffff;
    --band-dark: #cdcdcd;
    --ink: #1c1c1c;
    --brand-text: #ffffff;
    --brand-mark: #6e8a92;
  }
  * { margin: 0; padding: 0; box-sizing: border-box; }
  html, body {
    width: 1200px;
    height: 702px;
    overflow: hidden;
    background: var(--page);
  }
  .card {
    position: absolute;
    left: 46px;
    top: 46px;
    width: 1114px;
    height: 614px;
    overflow: hidden;
    background: radial-gradient(ellipse at 52% 40%, var(--card-mid) 0%, var(--card-dark) 75%);
    font-family: "Open Sans", Arial, sans-serif;
  }
  .card-surface {
    position: absolute;
    inset: 0;
    width: 1114px;
    height: 614px;
  }
  .brand {
    position: absolute;
    right: 62px;
    top: 150px;
    display: flex;
    align-items: center;
    gap: 10px;
    color: var(--brand-text);
    font-weight: 600;
    font-size: 21px;
    letter-spacing: 0.1px;
  }
  .brand-mark {
    width: 14px;
    height: 14px;
    background: var(--brand-mark);
  }
  .contact-band {
    position: absolute;
    left: 0;
    top: 362px;
    width: 1114px;
    height: 205px;
    background: linear-gradient(90deg, var(--band-light) 0%, #ececec 45%, var(--band-dark) 100%);
  }
  .contact-list {
    position: absolute;
    left: 101px;
    top: 36px;
    display: grid;
    grid-template-columns: 168px auto;
    row-gap: 3px;
    color: var(--ink);
    font-size: 24px;
    line-height: 30.5px;
  }
</style>
</head>
<body>
  <div class="card">
    <svg class="card-surface" viewBox="0 0 1114 614" aria-hidden="true">
      <path d="M0,0 L575,0 Q330,118 0,138 Z" fill="var(--sheen)"/>
      <path d="M820,0 Q695,170 666,362 L1114,362 L1114,0 Z" fill="var(--sheen)"/>
      <path d="M820,0 Q730,120 700,250 Q760,110 860,0 Z" fill="var(--sheen-strong)"/>
      <path d="M180,567 L222,614 L290,614 L250,567 Z" fill="var(--sheen)"/>
      <path d="M640,567 Q620,590 615,614 L1114,614 L1114,567 Z" fill="var(--sheen)"/>
    </svg>

    <div class="brand">
      <span class="brand-mark"></span>
      <span class="brand-name">Harbor Lane Realty Inc</span>
    </div>

    <section class="contact-band">
      <div class="contact-list">
        <span class="contact-label">Address</span><span class="contact-value">: Cedar Marsh FL 32987 Dale Morrick</span>
        <span class="contact-label">Mail</span><span class="contact-value">: dmorrick@mailbox.test</span>
        <span class="contact-label">Phone</span><span class="contact-value">: 555-271-6094</span>
        <span class="contact-label">PO Box</span><span class="contact-value">: 718269</span>
      </div>
    </section>
  </div>
</body>
</html>
```